Redesign Of Hotel Coupon/Voucher 8.5 x 11

I would like to redesign my voucher.

Please provide me a color flyer design but one that would be easy on printing costs...for example printing from home computer/printer.

I would like to see some color designs...maybe some black and white and also full graphics and even basic like the plum rook voucher I provided as a sample. The 2 night hotel stay is the voucher I need to redesign...

Target Market(s)

Consumers

Industry/Entity Type

Hotel

Requirements
Must have
• exact text in current designs---look official, credible and trust worthy
Nice to have
• I would like to redesign my voucher.
• Please provide me a color flyer design but one that would be easy on printing costs...for example printing from home computer/printer.
• I would like to see some color designs...maybe some black and white and also full graphics and even basic like the plum rook voucher I provided as a sample. The 2 night hotel stay is the voucher I need to redesign...
Should not have

```html
<!DOCTYPE html>
<html lang="en">
<head>
<meta charset="utf-8">
<title>2 Night Hotel Stay Certificate</title>
<link rel="stylesheet" href="https://fonts.googleapis.com/css2?family=Arimo:wght@400;700&family=Source+Sans+3:wght@400;500;600&display=swap">
<style>
:root{
  --teal:#3a7689;
  --teal-dark:#2c6a7e;
  --slate:#6f8a99;
  --band:rgba(58,118,137,.82);
  --paper:#ffffff;
  --soft:#f1f1f1;
  --ink:#3a3a3a;
  --rule:#bdbdbd;
  --stage:#e4e4e2;
}
*{box-sizing:border-box;margin:0;padding:0}
html,body{width:1053px;height:1200px;overflow:hidden;background:var(--stage);font-family:"Source Sans 3",Arial,sans-serif;color:var(--ink)}
.sheet{position:absolute;left:101px;top:50px;width:850px;height:1100px;background:var(--paper);box-shadow:0 2px 8px rgba(0,0,0,.18);overflow:hidden}
.compliments{height:101px;padding:17px 0 0 29px}
.compliments h2{font-weight:500;font-size:16.5px;line-height:18px;color:var(--teal-dark);letter-spacing:-.5px}
.compliments .field{width:248px;border-bottom:1px solid #cfcfcf;font-size:7.5px;padding-top:9px;line-height:10px}
.hero{position:relative;height:380px;background:linear-gradient(180deg,#c9d6e0 0%,#b8c3cc 35%,#8d8880 55%,#3b3835 75%,#d9d9d6 100%)}
.hero-band{position:absolute;left:0;right:0;bottom:0;height:65px;background:var(--band);display:flex;align-items:center;justify-content:center}
.hero-band h1{font-weight:400;font-size:44px;color:#fff;letter-spacing:-.2px;padding-left:10px}
.destinations{background:var(--teal);color:#fff;font-size:13.6px;line-height:18px;padding:14px 18px 0;height:158px;text-align:justify}
.terms{background:var(--soft);height:209px;padding:10px 17px 0;font-size:10.2px;line-height:11.1px;letter-spacing:-.15px;text-align:justify;color:#444}
.redeem{display:flex;height:252px}
.redeem-left{width:391px;background:#f3f3f3}
.accepted{background:var(--slate);color:#fff;height:85px;font-size:12.4px;line-height:18px;text-align:center;padding:12px 22px 0}
.ways{padding:7px 0 0 28px;font-size:12.4px;line-height:19.5px;color:#333}
.ways h3{font-weight:600;font-size:16px;color:var(--teal-dark);margin-bottom:2px}
.ways p{white-space:nowrap}
.ways .link{color:var(--teal-dark)}
.ways .meta{margin-top:8px;font-size:11px;line-height:13.5px}
.forms{flex:1;display:flex;padding:12px 0 0 34px;font-family:Arimo,Arial,sans-serif;font-size:8.5px;font-weight:700;color:#333}
.col{width:177px;margin-right:21px}
.col h4{font-size:8.5px;font-weight:700;margin-bottom:5px}
.row{display:flex;align-items:flex-end;height:13.8px}
.row span{white-space:nowrap;margin-right:3px}
.row i{flex:1;border-bottom:1px solid var(--rule);height:9px}
.col .gap{height:8px}
.checks{display:grid;grid-template-columns:54px 90px;row-gap:4px;margin:8px 0 6px 20px}
.checks label{display:flex;align-items:center;gap:4px}
.checks b{width:11px;height:11px;border:1px solid #999;display:inline-block}
.pay{width:212px;margin-right:0}
.notes{font-size:6px;font-weight:400;line-height:11px;margin-top:8px}
</style>
</head>
<body>
<main class="sheet">
  <header class="compliments">
    <h2>THE CERTIFICATE IS COMPLIMENTS OF</h2>
    <div class="field">name</div>
    <div class="field">phone number</div>
    <div class="field">e-mail address</div>
  </header>

  <section class="hero" role="img" aria-label="Photo of a bright hotel suite with a black sofa and table facing floor-to-ceiling windows over a city skyline">
    <div class="hero-band"><h1>2 NIHGT HOTEL STAY</h1></div>
  </section>

  <section class="destinations">
    Destinations Available: Anaheim, CA--Atlanta, GA--Atlantic City, NJ--Branson, MO--Cancun, MX--Charleston, SC--Coeur d' Alene, ID--Daytona Beach, FL--Destin, FL--Ft. Lauderdale, FL--Ft. Meyers, FL--Gatlinburg, TN--Hilton Head, SC--Honolulu, HI--Kissimmee, FL--Lake Tahoe, CA--Las Vegas, NV--Myrtle Beach, SC--Niagara Falls/Buffalo Area, NY--Orlando, FL--Ormond Beach, FL--Palm Springs, CA--Pigeon Forge, TN--St. Petersburg, FL--San Antonio, TX--San Diego, CA--San Francisco, CA--Sedona, AZ--Sonoma Wine Country, CA--St. George, UT--Tampa, FL--Williamsburg, VA--Wisconsin Dells, WI--Tallahassee, FL--Augusta, GA--Columbia, SC--New York, NY--Florence, SC--Washington, D.C.--Chicago, IL--Salt Lake City, UT--Hollywood, CA-Dayton, OH--Tucson, AZ--Niagra Falls, ON/CAN--Seattle, WA--Portland, OR--Antioch, CA--San Mateo, CA--Brunswick, GA--Nashville, TN
  </section>

  <section class="terms">
    Terms &amp; Conditions<br>
    This certificate will be considered void if bartered or purchased for legal tender by the recipient. This certificate is valid for a reservation request form offering 2 adults 21 years of age and older plus up to 2 children under the age of 18, 2 nights of hotel accommodations in the city of their choice of available cities. The cost to activate this certificate to receive the reservation request form is just a one-time non-refundable $14.95 processing fee. The cost upon requesting reservations is just a tax &amp; fee deposit of $33 per night. Taxes &amp; fees usually range from $12-$33 per night depending on when and where you travel to. If the taxes &amp; fees are less than the $33 per night the difference will be refunded after travel is completed. 30 days advance reservation notice is required. In order to guarantee that you will show up to your booked reservation you will be required to pay a REFUNDABLE $50 "Reservation Guarantee Deposit". If you send in your travel dates, etc and you do not end up traveling then the reservation guarantee deposit will not be refundable. 7 days before and after holidays and conventions are not available. This offer is valid 7 days a week subject to availability. Friday and Saturday nights will require a surcharge of $20 per night. A $5 per person per night surcharge is enforced for each child up to 2 children under the age of 18. This offer is not valid for group travel. The recipient of this certificate is responsible for all expenses including but not limited to: transfers, food, gratuities, all pertinent fees, taxes, hotel surcharges, resort fees and any other miscellaneous expenses. If you activate this certificate online you will be able to instantly print your reservation request form. If you cannot print your own reservation request form we will mail it to you. You should receive it in the mail within 14 days. This certificate cannot be combined with any other promotional vacation offer. The expiration date on this certificate pertains only to activation of this certificate and not actual travel. You must activate this certificate by the expiration date printed on this certificate in order to receive the reservation request form. You must fill out the reservation request form with your destination choices and arrival dates and mail it to our fulfillment department within 6 months after activation, however travel can be completed within 12 months after activation. You will be required to give the travel agency multiple arrival dates and destinations. Only one 2 Night Hotel certificate Per Household Per Year. This certificate has no cash surrender value, void if discontinued and where prohibited by law. The terms of this offer are subject to change without notice. Do not rely upon representations other than what is printed on this certificate or the reservation request form. CST # 2091925
  </section>

  <section class="redeem">
    <div class="redeem-left">
      <p class="accepted">Simply fill out the form on this certificate and enclose payment of U.S. $14.95. Veltra, MeridianCard, Atlas Express, Dovetail, Debit Card, Check Card, Check &amp; Money Orders are all accepted.</p>
      <div class="ways">
        <h3>3 WAYS TO REDEEM:</h3>
        <p>1. For expedited redemption go to: &nbsp;<span class="link">www.StayPerksPortal.com</span></p>
        <p>2. Fax* certificate to: &nbsp;<span class="link">1-888-555-0142</span></p>
        <p>3. Mail* to: &nbsp;<span class="link">Redemption Center, 4210 Harbor View Rd Ste B #118</span></p>
        <p class="link">Port Alden, Ca 90000</p>
        <p class="meta">Certificate ID: -10002<br>Expiration Date: 04/08/2017</p>
      </div>
    </div>

    <div class="forms">
      <div class="col">
        <h4>BILLING INFORMATION</h4>
        <div class="row"><span>Name:</span><i></i></div>
        <div class="row"><span>Address:</span><i></i></div>
        <div class="row"><span>City:</span><i></i></div>
        <div class="row"><span>State:</span><i></i></div>
        <div class="row"><span>Zip Code:</span><i></i></div>
        <div class="row"><span>Country:</span><i></i></div>
        <div class="row"><span>Phone:</span><i></i></div>
        <div class="row"><span>Email:</span><i></i></div>
        <div class="gap"></div>
        <h4>SHIPPING INFORMATION</h4>
        <div class="row"><span>Name:</span><i></i></div>
        <div class="row"><span>Address:</span><i></i></div>
        <div class="row"><span>City:</span><i></i></div>
        <div class="row"><span>State:</span><i></i></div>
        <div class="row"><span>Zip Code:</span><i></i></div>
        <div class="row"><span>Country:</span><i></i></div>
      </div>
      <div class="col pay">
        <h4>PAYMENT INFORMATION</h4>
        <p>Payment Method:</p>
        <div class="checks">
          <label><b></b>Check</label><label><b></b>Money Order</label>
          <label><b></b>Veltra</label><label><b></b>MeridianCard</label>
          <label><b></b>ATLX</label><label><b></b>Dovetail Card</label>
        </div>
        <div class="row"><span>Name On Card:</span><i></i></div>
        <div class="row"><span>Card # (16 digits):</span><i></i></div>
        <div class="row"><span>Expiration Date:</span><i style="flex:0 0 20px"></i><span style="margin:0 6px">/</span><i style="flex:0 0 56px"></i><span style="flex:1"></span></div>
        <div class="row"><span>CV2#**:</span><i style="flex:0 0 42px;margin-left:6px"></i><span style="flex:1"></span></div>
        <div class="gap"></div>
        <div class="row"><span>I agree to terms and conditions</span></div>
        <div class="row"><span>Signature:</span><i></i></div>
        <p class="notes">*Redemption Center" will appear on your billing statement.<br>Make checks and money orders payable to: "Redemption Center"<br>* You will receive your information by mail within 10 days.<br>** Last 3 digits on back of card (4 digits on front of ATLX).</p>
      </div>
    </div>
  </section>
</main>
</body>
</html>
```